New Business Card for General Contractor Marketing

Need a business card the is more like a marketing promotion of our services
Must be horizontal orientation, One Sided Only, Max font size, Organize the Services
#1 General Contractor for Realtors
Remodels – Renovations – Repairs
Water & Mold Damage Experts
Painting: Interior/ Exterior
Flooring: Wood / LVT / Carpet
Plumbing: Repairs & Upgrades
Electric: Lights & Energy Efficient Upgrades
Kitchen & Bath Remodels
Fast Inspections Repair Billed Thru Escrow
BrightHarborBuild.example
555-014-7390

Industry/Entity Type

General Contractor

Contact Information for Business Card

One Sided Only: #1 General Contractor for Realtors Remodels – Renovations – Repairs Water & Mold Damage Experts Painting: Interior/ Exterior Flooring: Wood / LVT / Carpet Plumbing: Repairs & Upgrades Electric: Lights & Energy Efficient Upgrades Kitchen & Bath Remodels Fast Inspections Repair Billed Thru Escrow BrightHarborBuild.example 555-014-7390

Colors
0054AA
0677BA
7BADD7
CADEEF
E8F1F8

Requirements
Must have
• One Sided Only: #1 General Contractor for Realtors Remodels – Renovations – Repairs Water & Mold Damage Experts Painting: Interior/ Exterior Flooring: Wood / LVT / Carpet Plumbing: Repairs & Upgrades Electric: Lights & Energy Efficient Upgrades Kitchen & Bath Remodels Fast Inspections Repair Billed Thru Escrow BrightHarborBuild.example 555-014-7390

```html
<!DOCTYPE html>
<html lang="en">
<head>
<meta charset="UTF-8">
<title>Contractor Business Card</title>
<link href="https://fonts.googleapis.com/css2?family=Montserrat:wght@700;800&display=swap" rel="stylesheet">
<style>
  :root {
    --navy: #0e3472;
    --navy-deep: #0a2d66;
    --orange: #f26b0f;
    --orange-deep: #e05a06;
    --sky-edge: #9fcaf1;
    --sky-mid: #dcecfa;
    --white: #ffffff;
    --phone-gold: #f6b35e;
  }
  * { margin: 0; padding: 0; box-sizing: border-box; }
  html, body {
    width: 1200px; height: 800px; overflow: hidden;
    background: var(--white);
  }
  .card {
    position: relative;
    width: 1200px; height: 800px;
    overflow: hidden;
    font-family: 'Montserrat', sans-serif;
    background: radial-gradient(ellipse 70% 65% at 50% 48%, var(--white) 0%, var(--sky-mid) 60%, var(--sky-edge) 100%);
  }
  .hero-art {
    position: absolute;
    left: 420px; top: 22px;
    width: 360px; height: 170px;
    border-radius: 12px;
    background: linear-gradient(180deg, #c9d6ea 0%, #f3c59f 100%);
  }
  .headline-band {
    position: absolute;
    left: 62px; top: 204px;
    width: 1072px; height: 66px;
    background: linear-gradient(90deg, var(--orange-deep), var(--orange) 50%, var(--orange-deep));
    clip-path: polygon(2.5% 0, 100% 0, 97.5% 100%, 0 100%);
    display: flex; align-items: center; justify-content: center;
  }
  .headline {
    color: var(--white);
    font-weight: 800;
    font-size: 43px;
    letter-spacing: -0.5px;
    white-space: nowrap;
  }
  .services {
    position: absolute;
    left: 118px; top: 278px;
    list-style: none;
  }
  .service {
    display: flex; align-items: center;
    height: 48px;
    color: var(--navy);
    font-weight: 800;
    font-size: 34px;
    white-space: nowrap;
    letter-spacing: -0.3px;
  }
  .service.is-lead { font-size: 40px; height: 54px; }
  .service .tick { width: 36px; height: 36px; margin-right: 14px; flex: none; }
  .escrow-band {
    position: absolute;
    left: 89px; top: 648px;
    width: 1008px; height: 56px;
    background: linear-gradient(90deg, var(--orange-deep), var(--orange) 50%, var(--orange-deep));
    clip-path: polygon(3% 0, 100% 0, 97% 100%, 0 100%);
    display: flex; align-items: center; justify-content: center;
  }
  .escrow {
    color: var(--white);
    font-weight: 800;
    font-size: 33px;
    white-space: nowrap;
  }
  .footer {
    position: absolute;
    left: 0; top: 714px;
    width: 1200px; height: 86px;
    background: linear-gradient(90deg, #7fb8ee 0%, #cfe4f8 40%, #e8f2fb 100%);
  }
  .footer-contact {
    position: absolute;
    right: 0; top: 0;
    width: 545px; height: 86px;
    background: var(--navy-deep);
    clip-path: polygon(7% 0, 100% 0, 100% 100%, 0 100%);
    display: flex; align-items: center; justify-content: center;
    padding-left: 20px;
  }
  .website {
    position: absolute;
    left: 105px; top: 0; height: 86px;
    display: flex; align-items: center;
    color: var(--navy);
    font-weight: 700;
    font-size: 39px;
    letter-spacing: -0.5px;
  }
  .phone {
    display: flex; align-items: center;
    color: var(--phone-gold);
    font-weight: 800;
    font-size: 40px;
  }
  .phone svg { width: 34px; height: 34px; margin-right: 10px; }
</style>
</head>
<body>
  <div class="card">
    <div class="hero-art" role="img" aria-label="Illustration of house rooftops with a worker, ladder, paint roller and wrench"></div>

    <div class="headline-band">
      <h1 class="headline">#1 GENERAL CONTRACTOR FOR REALTORS</h1>
    </div>

    <ul class="services">
      <li class="service is-lead">
        <svg class="tick" viewBox="0 0 40 40"><circle cx="20" cy="20" r="19" fill="var(--orange)"/><path d="M11 20.5l6 6 12-13" fill="none" stroke="#fff" stroke-width="5" stroke-linecap="round" stroke-linejoin="round"/></svg>
        Remodels – Renovations – Repairs
      </li>
      <li class="service is-lead">
        <svg class="tick" viewBox="0 0 40 40"><circle cx="20" cy="20" r="19" fill="var(--orange)"/><path d="M11 20.5l6 6 12-13" fill="none" stroke="#fff" stroke-width="5" stroke-linecap="round" stroke-linejoin="round"/></svg>
        Water &amp; Mold Damage Experts
      </li>
      <li class="service">
        <svg class="tick" viewBox="0 0 40 40"><circle cx="20" cy="20" r="19" fill="var(--orange)"/><path d="M11 20.5l6 6 12-13" fill="none" stroke="#fff" stroke-width="5" stroke-linecap="round" stroke-linejoin="round"/></svg>
        Painting: Interior / Exterior
      </li>
      <li class="service">
        <svg class="tick" viewBox="0 0 40 40"><circle cx="20" cy="20" r="19" fill="var(--orange)"/><path d="M11 20.5l6 6 12-13" fill="none" stroke="#fff" stroke-width="5" stroke-linecap="round" stroke-linejoin="round"/></svg>
        Flooring: Wood / LVT / Carpet
      </li>
      <li class="service">
        <svg class="tick" viewBox="0 0 40 40"><circle cx="20" cy="20" r="19" fill="var(--orange)"/><path d="M11 20.5l6 6 12-13" fill="none" stroke="#fff" stroke-width="5" stroke-linecap="round" stroke-linejoin="round"/></svg>
        Plumbing: Repairs &amp; Upgrades
      </li>
      <li class="service">
        <svg class="tick" viewBox="0 0 40 40"><circle cx="20" cy="20" r="19" fill="var(--orange)"/><path d="M11 20.5l6 6 12-13" fill="none" stroke="#fff" stroke-width="5" stroke-linecap="round" stroke-linejoin="round"/></svg>
        Electric: Lights &amp; Energy Efficient Upgrades
      </li>
      <li class="service">
        <svg class="tick" viewBox="0 0 40 40"><circle cx="20" cy="20" r="19" fill="var(--orange)"/><path d="M11 20.5l6 6 12-13" fill="none" stroke="#fff" stroke-width="5" stroke-linecap="round" stroke-linejoin="round"/></svg>
        Kitchen &amp; Bath Remodels
      </li>
    </ul>

    <div class="escrow-band">
      <p class="escrow">Fast Inspections Repair Billed Thru Escrow</p>
    </div>

    <footer class="footer">
      <span class="website">BrightHarborBuild.example</span>
      <div class="footer-contact">
        <span class="phone">
          <svg viewBox="0 0 24 24"><path fill="#ffffff" d="M6.6 10.8a15.1 15.1 0 0 0 6.6 6.6l2.2-2.2a1 1 0 0 1 1-.25 11.4 11.4 0 0 0 3.6.57 1 1 0 0 1 1 1V20a1 1 0 0 1-1 1A17 17 0 0 1 3 4a1 1 0 0 1 1-1h3.5a1 1 0 0 1 1 1c0 1.25.2 2.45.57 3.6a1 1 0 0 1-.25 1z"/></svg>
          555-014-7390
        </span>
      </div>
    </footer>
  </div>
</body>
</html>
```